依頼概要
ふわりやと言うめろんぱんチェンーのキャンペーン商品のポスター依頼です。
昨年も販売した商品で今年も6月から期間限定で販売します。
商品名 小春ミントメロンパン
売価  320円
サイズ B2
ポスターに求める事は、夏場の暑い時期に見ても、さっぱりした感じのするポスターをお願いしたいと思います。店舗と商品のイメージはHPをご覧になって下さい。
ファイルは、そのままネット印刷会社に依頼できる状態のファイルとCS2で編集可能なアウトライン前のファイルと出して頂ける事を条件とします。

瀬戸内のブランドイメージの表現と夏の感じが強く感じられ、商品も遠目から瞬間的に認識で、訴求につながると選考したスッタフの意見となりました。

沢山のご応募頂き有難うございました。
最終の選考に5人の方を絞り、いずれもお願いしたいくらい素晴らし作品でした。また次は、秋の商品・新商品を検討しております。
今後とも宜しくお願い致します。

```html
<!DOCTYPE html>
<html lang="ja">
<head>
<meta charset="utf-8">
<title>小春ミントメロンパン 限定販売</title>
<link href="https://fonts.googleapis.com/css2?family=M+PLUS+Rounded+1c:wght@500;800;900&display=swap" rel="stylesheet">
<style>
  :root {
    --sky: #a9ddf3;
    --sky-deep: #3fa6d8;
    --cream: #fffbe6;
    --butter: #fff0a8;
    --lemon: #ffe14a;
    --border-blue: #cfeaf6;
    --border-yellow: #fbf1b8;
    --magenta: #e0408f;
    --ink: #3a3a3a;
    --white: #ffffff;
    --bread: #f1cf4a;
    --brown: #8a6a2a;
    --grey: #6a6a6a;
  }
  * { margin: 0; padding: 0; box-sizing: border-box; }
  html, body { width: 849px; height: 1200px; overflow: hidden; }
  body {
    font-family: "M PLUS Rounded 1c", sans-serif;
    color: var(--ink);
  }
  .poster {
    position: relative;
    width: 849px;
    height: 1200px;
    background: linear-gradient(135deg, var(--border-blue), var(--border-yellow) 50%, var(--border-blue));
    padding: 26px;
  }
  .panel {
    position: relative;
    width: 100%;
    height: 100%;
    overflow: hidden;
    background: linear-gradient(180deg, var(--sky) 0%, #d8f0fa 35%, var(--cream) 70%, var(--butter) 100%);
  }
  .title {
    position: absolute;
    top: 22px;
    left: 0;
    width: 100%;
    text-align: center;
    font-weight: 900;
    font-size: 96px;
    line-height: 120px;
    color: var(--white);
    letter-spacing: 2px;
    text-shadow: 0 0 10px rgba(63,166,216,0.55), 3px 3px 0 var(--sky-deep);
  }
  .title .accent { color: var(--lemon); }
  .limited {
    position: absolute;
    top: 292px;
    left: 50%;
    transform: translateX(-50%);
    width: 254px;
    height: 68px;
    border: 4px solid var(--magenta);
    border-radius: 34px;
    background: var(--white);
    color: var(--magenta);
    font-weight: 800;
    font-size: 36px;
    line-height: 60px;
    text-align: center;
    letter-spacing: 6px;
  }
  .product-visual {
    position: absolute;
    top: 390px;
    left: 90px;
    width: 617px;
    height: 460px;
    border-radius: 50%;
    background: radial-gradient(circle at 50% 45%, var(--bread) 0%, #f5dc70 45%, rgba(255,240,168,0) 72%);
  }
  .copy {
    position: absolute;
    top: 892px;
    left: 0;
    width: 100%;
    text-align: center;
    font-weight: 500;
    font-size: 25px;
    line-height: 42px;
    letter-spacing: 1px;
  }
  .brand {
    position: absolute;
    left: 30px;
    bottom: 62px;
    display: flex;
    align-items: center;
    gap: 10px;
  }
  .brand-dot {
    width: 38px;
    height: 38px;
    border-radius: 50%;
    background: var(--lemon);
  }
  .brand-name {
    font-weight: 800;
    font-size: 40px;
    line-height: 1.1;
    color: var(--brown);
  }
  .brand-tagline {
    position: absolute;
    left: 82px;
    bottom: 44px;
    font-size: 11px;
    color: var(--brown);
  }
  .note {
    position: absolute;
    left: 30px;
    bottom: 18px;
    font-size: 13px;
    color: var(--grey);
  }
  .price {
    position: absolute;
    right: 30px;
    bottom: 28px;
    display: flex;
    align-items: flex-end;
    font-weight: 900;
    color: var(--ink);
  }
  .price-yen { font-size: 56px; line-height: 1; margin-bottom: 6px; }
  .price-num { font-size: 88px; line-height: 0.9; }
  .price-unit { font-size: 40px; line-height: 1; margin-bottom: 6px; }
  .price-tax {
    margin-left: 6px;
    margin-bottom: 10px;
    background: var(--lemon);
    font-size: 20px;
    font-weight: 800;
    padding: 6px 6px;
    line-height: 1;
  }
</style>
</head>
<body>
  <div class="poster">
    <div class="panel">
      <h1 class="title"><span>小春</span><span class="accent">ミント</span><br>メロンパン</h1>
      <div class="limited">限定販売</div>
      <div class="product-visual" role="img" aria-label="ホイップクリームをサンドしたメロンパンと輪切りの果実のイラスト"></div>
      <p class="copy">爽やかな香りの小春ミントと<br>ホイップクリームをふわりやメロンに<br>サンドしました</p>
      <div class="brand">
        <span class="brand-dot"></span>
        <span class="brand-name">ふわりや</span>
      </div>
      <div class="brand-tagline">Soft Sweet Melon Bread</div>
      <p class="note">※写真・イラストはイメージです。</p>
      <div class="price">
        <span class="price-yen">¥</span>
        <span class="price-num">320</span>
        <span class="price-unit">円</span>
        <span class="price-tax">税込</span>
      </div>
    </div>
  </div>
</body>
</html>
```